KWI Business Card

Please create a creative design for a business card using the new theme from the Logo & website. This company's main focus is food manufacturing building construction. Please integrate the new logo attached.

Please use the following information for the demo card:

Korvel Walls, Inc.
Dana Whitcombe
dwhitcombe@korvelwalls.example
Cell: 312-555-0178
218 Larkmoor Ave
Brennick, IL 60418

See pictures and more information on the website.

www.korvelwalls.example

```html
<!DOCTYPE html>
<html lang="en">
<head>
<meta charset="utf-8">
<title>KWI Business Card</title>
<link href="https://fonts.googleapis.com/css2?family=Open+Sans:wght@400;600;700&display=swap" rel="stylesheet">
<style>
  :root {
    --stage: #0e4e70;
    --navy: #132a4a;
    --blue: #2f72b8;
    --sky: #4a8fd6;
    --paper: #f3f4f5;
    --ink-light: #eaf2fb;
  }
  * { margin: 0; padding: 0; box-sizing: border-box; }
  html, body { width: 1200px; height: 800px; overflow: hidden; }
  body {
    background: var(--stage);
    font-family: "Open Sans", sans-serif;
    display: flex;
    align-items: center;
    justify-content: center;
    gap: 40px;
  }
  .card {
    position: relative;
    width: 540px;
    height: 308px;
    overflow: hidden;
    box-shadow: 0 10px 24px rgba(0,0,0,0.35);
  }
  .card-art { position: absolute; inset: 0; }
  .contact-block {
    position: absolute;
    left: 34px;
    top: 34px;
    width: 290px;
  }
  .holder-name {
    color: var(--navy);
    font-size: 25px;
    font-weight: 600;
    letter-spacing: 0.5px;
    text-transform: uppercase;
    line-height: 1.1;
  }
  .holder-company {
    color: var(--navy);
    font-size: 13px;
    text-align right;
    text-align: right;
    padding-right: 26px;
    margin-top: 2px;
  }
  .contact-list { list-style: none; margin-top: 22px; }
  .contact-item {
    display: flex;
    align-items: center;
    gap: 12px;
    color: var(--ink-light);
    font-size: 13px;
    line-height: 1.3;
    margin-bottom: 11px;
  }
  .contact-icon { flex: 0 0 30px; width: 30px; height: 30px; }
  .wordmark {
    position: absolute;
    display: flex;
    align-items: center;
    gap: 8px;
  }
  .wordmark-mark { background: var(--sky); }
  .wordmark-name {
    font-weight: 700;
    letter-spacing: 2px;
    line-height: 1;
  }
  .card-front .wordmark { right: 22px; top: 158px; }
  .card-front .wordmark-mark { width: 12px; height: 12px; }
  .card-front .wordmark-name { font-size: 44px; color: var(--blue); }
  .card-back .wordmark { right: 60px; top: 160px; }
  .card-back .wordmark-mark { width: 20px; height: 20px; }
  .card-back .wordmark-name { font-size: 84px; color: var(--sky); }
</style>
</head>
<body>

<section class="card card-front">
  <svg class="card-art" viewBox="0 0 540 308" aria-hidden="true">
    <rect width="540" height="308" fill="var(--blue)"/>
    <polygon points="300,0 335,0 410,308 345,308" fill="var(--navy)"/>
    <polygon points="322,0 335,0 410,308 392,308" fill="var(--sky)"/>
    <polygon points="335,0 540,0 540,308 410,308" fill="var(--paper)"/>
  </svg>

  <div class="contact-block">
    <h1 class="holder-name">Dana Whitcombe</h1>
    <p class="holder-company">Korvel Walls, Inc.</p>
    <ul class="contact-list">
      <li class="contact-item">
        <svg class="contact-icon" viewBox="0 0 30 30"><circle cx="15" cy="15" r="15" fill="var(--navy)"/><path d="M11 8c1 0 2 3 2 4s-1 1-1 2 3 4 4 4 1-1 2-1 4 1 4 2-2 3-3 3c-5 0-10-6-10-11 0-1 1-3 2-3z" fill="#fff"/></svg>
        <span>312-555-0178</span>
      </li>
      <li class="contact-item">
        <svg class="contact-icon" viewBox="0 0 30 30"><circle cx="15" cy="15" r="15" fill="var(--navy)"/><rect x="8" y="10" width="14" height="10" fill="none" stroke="#fff" stroke-width="1.6"/><path d="M8 10l7 6 7-6" fill="none" stroke="#fff" stroke-width="1.6"/></svg>
        <span>dwhitcombe@korvelwalls.example</span>
      </li>
      <li class="contact-item">
        <svg class="contact-icon" viewBox="0 0 30 30"><circle cx="15" cy="15" r="15" fill="var(--navy)"/><path d="M15 7a5.5 5.5 0 0 1 5.5 5.5c0 4-5.5 10-5.5 10s-5.5-6-5.5-10A5.5 5.5 0 0 1 15 7z" fill="#fff"/><circle cx="15" cy="12.5" r="2" fill="var(--navy)"/></svg>
        <span>218 Larkmoor Ave<br>Brennick, IL 60418</span>
      </li>
      <li class="contact-item">
        <svg class="contact-icon" viewBox="0 0 30 30"><circle cx="15" cy="15" r="15" fill="var(--navy)"/><g fill="none" stroke="#fff" stroke-width="1.3"><circle cx="15" cy="15" r="7"/><ellipse cx="15" cy="15" rx="3" ry="7"/><path d="M8 15h14M9 11.5h12M9 18.5h12"/></g></svg>
        <span>www.korvelwalls.example</span>
      </li>
    </ul>
  </div>

  <div class="wordmark">
    <span class="wordmark-mark"></span>
    <span class="wordmark-name">KWI</span>
  </div>
</section>

<section class="card card-back">
  <svg class="card-art" viewBox="0 0 540 308" aria-hidden="true">
    <rect width="540" height="308" fill="var(--navy)"/>
    <polygon points="0,150 340,0 410,0 0,215" fill="var(--blue)"/>
    <polygon points="0,0 340,0 0,150" fill="var(--paper)"/>
  </svg>
  <div class="wordmark">
    <span class="wordmark-mark"></span>
    <span class="wordmark-name">KWI</span>
  </div>
</section>

</body>
</html>
```